Business Card

I need a business card that is fresh, styling and reflects my heart centered healing business while still maintaining full professionalism as I have an my evidence-based practice. I am a Naturopath and a Shiatsu Massage Therapist.
Below are my existing logo (file 1) and an inspiration image (file 2) that reflects the colours and style I would like to express to my card (blues greens). I especially like that tree wallpaper.

Information for the card:
Maren Throsby
BHSc. (Nat) m.ROSC
Naturopath
Herbalist
Nutritionist
Shiatsu Therapist
Wellness Counsellor

47 Dunmore St South Fremantle
www.marenthrosby-demo.com.au
maren@marenthrosby-demo.com.au

NOte: I've removed part of the brief, in that I've changed my mind about the back of the card being a '5 treatments and get sixth one free" I'd rather have this on a separate card. So please do not include this in your designs.

Hi Guys, I've taken the '5 session get the sixth free' part out of the brief. Also, I've added the info to go on the business card into the brief.

Thanks and happy designing
Mar

I've just uploaded a high res better quality version of the hand logo. Thanks Lovlies. 

Target Market(s)

I am targeting western women of ages 25 - 40 in preconception care, sugar addiction therapy, and wellness coaching. I want must card to be vibrant, positive and current.

Industry/Entity Type

Business

Requirements
Must have
• Please include my hand image logo

```html
<!DOCTYPE html>
<html lang="en">
<head>
<meta charset="utf-8">
<title>Maren Throsby – Business Card</title>
<link rel="stylesheet" href="https://fonts.googleapis.com/css2?family=Antonio:wght@100;200;300&display=swap">
<style>
  :root {
    --page: #ffffff;
    --frame: #4a4a4a;
    --ink: #222222;
    --navy: #3d4fa1;
    --sky: #8dd4f4;
    --mint: #b5dfc9;
    --sage: #a8c9a8;
    --lime: #c6e09c;
    --dash: #a9d06a;
    --sand: #dfc39c;
  }
  * { box-sizing: border-box; margin: 0; padding: 0; }
  html, body {
    width: 1200px; height: 1000px; overflow: hidden;
    background: var(--page);
    font-family: "Antonio", "Arial Narrow", sans-serif;
  }
  .card {
    position: absolute; left: 241px; width: 731px; height: 420px;
    border: 4px solid var(--frame); border-radius: 4px;
    background: var(--page); overflow: hidden;
  }
  .card--back { top: 56px; }
  .card--front { top: 514px; }

  .pattern { position: absolute; top: 0; height: 100%; }
  .card--back .pattern {
    right: 0; width: 208px;
    background: linear-gradient(160deg, var(--sage) 0%, var(--mint) 30%, var(--sky) 50%, var(--lime) 70%, var(--sage) 100%);
  }
  .card--front .pattern {
    left: 0; width: 300px;
    background: radial-gradient(ellipse at 50% 50%, var(--mint) 0%, var(--sage) 40%, var(--sky) 70%, var(--lime) 100%);
  }

  .contact { position: absolute; left: 98px; top: 96px; color: var(--ink); }
  .contact__phone {
    display: flex; align-items: center; gap: 12px;
    font-weight: 100; font-size: 76px; line-height: 1; letter-spacing: 0;
  }
  .contact__phone svg { width: 24px; height: 58px; }
  .contact__line {
    font-weight: 100; font-size: 26px; line-height: 1.25; text-transform: uppercase;
    letter-spacing: 0.3px;
  }
  .contact__address { margin-top: 6px; font-size: 28px; }
  .contact__rule {
    width: 344px; margin: 12px 0 14px 6px;
    border-top: 5px dashed var(--dash);
  }

  .brand-mark {
    position: absolute; left: 95px; top: 186px;
    display: flex; align-items: center; gap: 10px;
    padding: 8px 14px; background: var(--page); border-radius: 6px;
  }
  .brand-mark__dot { width: 22px; height: 22px; border-radius: 50%; background: var(--navy); }
  .brand-mark__name { font-weight: 300; font-size: 28px; line-height: 1; color: var(--navy); text-transform: uppercase; }

  .identity { position: absolute; left: 325px; top: 162px; color: var(--navy); }
  .identity__name {
    font-weight: 100; font-size: 62px; line-height: 1; text-transform: uppercase; letter-spacing: 1px;
  }
  .identity__role {
    font-weight: 200; font-size: 22px; text-transform: uppercase; margin-top: 2px; letter-spacing: 0.2px;
  }
  .birds {
    position: absolute; left: 370px; top: 272px; width: 160px; height: 72px;
    border-radius: 50%;
    background: radial-gradient(ellipse at 40% 50%, var(--sky) 0%, var(--sky) 35%, rgba(141,212,244,0) 70%);
  }
</style>
</head>
<body>
  <section class="card card--back">
    <div class="contact">
      <div class="contact__phone">
        <svg viewBox="0 0 26 62" aria-hidden="true">
          <path d="M20 2 C8 4 2 18 2 31 C2 44 8 58 20 60 L24 48 C18 46 15 39 15 31 C15 23 18 16 24 14 Z" fill="var(--sky)"/>
        </svg>
        <span>0412558047</span>
      </div>
      <p class="contact__line contact__address">47 Dunmore St South Fremantle</p>
      <div class="contact__rule"></div>
      <p class="contact__line">maren@marenthrosby-demo.com.au</p>
      <p class="contact__line">www.marenthrosby-demo.com.au</p>
    </div>
    <div class="pattern" role="img" aria-label="Decorative leaf pattern in blues and greens"></div>
  </section>

  <section class="card card--front">
    <div class="pattern" role="img" aria-label="Decorative leaf mandala in blues and greens"></div>
    <div class="brand-mark">
      <span class="brand-mark__dot"></span>
      <span class="brand-mark__name">Mar</span>
    </div>
    <div class="identity">
      <h1 class="identity__name">Maren Throsby</h1>
      <p class="identity__role">Naturopath &amp; Shiatsu Massage Therapist</p>
    </div>
    <div class="birds" role="img" aria-label="Small illustration of two birds in flight"></div>
  </section>
</body>
</html>
```